Online trading school - Website design

We are building an online trading school (trading of shares, commodities, indices, currencies). The purpose is to teach online traders how to trade successfully. We need to design the homepage of the website and logo (bramwelloq.com will be the domain). The homepage will contain the following elements

- logo
- Sign in and Register links/buttons
- upper menu
- short introduction
- a couple of bullet points 'Why to join our school?'
- sign up form
- text
- bottom menu

Attached is a draft for the designer. The draft is just for an inspiration, the actual structure of the website can be different if the designer thinks so.

The designer is free to choose colors.

School

3 page

```html
<!DOCTYPE html>
<html lang="en">
<head>
<meta charset="utf-8">
<title>Bramwelloq – Online Trading School</title>
<link href="https://fonts.googleapis.com/css2?family=Cabin:wght@400;500;700&family=Cabin+Condensed:wght@400;700&display=swap" rel="stylesheet">
<style>
  :root{
    --ink:#1d1d1f;
    --header:#232324;
    --nav:#2b2b2c;
    --nav-text:#d8d8d8;
    --accent:#ec6a5e;
    --light:#eceef2;
    --muted:#5a5a60;
    --offer:#a59fb4;
    --footer:#36363a;
    --link:#46a9b8;
    --white:#ffffff;
  }
  *{box-sizing:border-box;margin:0;padding:0}
  html,body{width:854px;height:1200px;overflow:hidden}
  body{position:relative;font-family:"Cabin",sans-serif;color:var(--ink);background:var(--white)}
  .abs{position:absolute}

  .site-header{left:0;top:0;width:854px;height:63px;background:var(--header);border-bottom:1px solid #bbb}
  .brand{left:74px;top:12px;font-size:32px;color:#f2ece2;font-weight:400}
  .social{display:flex;gap:14px;font-size:11px;color:#8a8a8e;align-items:center}
  .social span{display:flex;align-items:center;gap:4px}
  .social i{width:8px;height:8px;border-radius:50%;background:#8a8a8e;display:inline-block}
  .header-social{right:50px;top:26px}

  .main-nav{left:0;top:64px;width:854px;height:26px;background:var(--nav)}
  .main-nav a{position:absolute;top:4px;font-size:14px;color:var(--nav-text);text-decoration:none}

  .hero{left:0;top:90px;width:854px;height:252px;
    background:radial-gradient(ellipse at 8% 110%,#c98a5a 0%,#7a4a5e 25%,transparent 55%),
      linear-gradient(120deg,#3a2a4a 0%,#2a1a3c 45%,#1f1030 100%)}
  .hero-title{left:217px;top:145px;width:420px;height:46px;border:2px solid #e8e4ee;color:var(--white);
    font-size:35px;text-align:center;line-height:40px;letter-spacing:.5px}
  .hero-text{left:282px;top:204px;width:290px;color:#e6e2ec;font-size:9.6px;line-height:22px;text-align:center}
  .btn{background:var(--accent);color:var(--white);border-radius:9px;text-align:center}
  .hero-btn{left:388px;top:275px;width:78px;height:20px;font-size:12px;line-height:20px}

  .why{left:0;top:342px;width:854px;height:350px;background:var(--light);overflow:hidden}
  .why-mark{left:30px;top:60px;font-size:190px;color:rgba(0,0,0,.035);white-space:nowrap}
  .why-title{left:183px;top:56px;font-family:"Cabin Condensed",sans-serif;font-weight:700;font-size:21px}
  .why-list{left:159px;top:103px;list-style:none;color:var(--muted);font-size:18px}
  .why-list li{height:40px}

  .signup{left:540px;top:371px;width:236px;height:289px;border:2px solid #222;border-radius:4px}
  .signup h2{position:absolute;left:12px;top:20px;font-size:15px;font-weight:400}
  .field{position:absolute;left:12px;width:212px;height:23px;border:2px solid #222;border-radius:2px;
    font-size:14px;color:#9a9aa0;padding:2px 7px;background:transparent}
  .agree{left:28px;top:165px;font-size:11px;color:#555;display:flex;align-items:center;gap:6px}
  .agree i{width:11px;height:11px;border:1.5px solid #333;display:block}
  .submit{left:131px;top:199px;width:89px;height:21px;font-size:15px;line-height:21px}
  .member{left:30px;top:249px;font-size:16px}
  .member a{color:var(--link)}

  .offer{left:0;top:692px;width:854px;height:455px;background:var(--offer);border-top:1px solid #8a8494}
  .offer-title{left:0;top:24px;width:854px;text-align:center;font-size:34px;letter-spacing:.5px}
  .card{width:200px;text-align:center}
  .card-photo{display:block;margin:0 auto;width:152px;height:146px;border-radius:42%;border:3px solid #d9d7de}
  .card h3{font-weight:400;font-size:24px;margin-top:22px}
  .card p{width:118px;margin:12px auto 0;font-size:11px;line-height:13.5px;letter-spacing:1px;color:#333}

  .site-footer{left:0;top:1147px;width:854px;height:53px;background:var(--footer)}
  .copy{left:36px;top:20px;font-size:11px;color:#e8e8e8;line-height:12px;letter-spacing:.6px}
  .copy b{color:#7fd0e0;font-weight:400}
  .copy small{display:block;color:#aaa;font-size:11px;margin-left:18px}
  .footer-social{left:372px;top:22px}
  .legal{right:36px;top:20px;font-size:11px;color:#eee;letter-spacing:.6px}
  .legal a{color:#eee}
</style>
</head>
<body>
  <header class="abs site-header">
    <div class="abs brand">Bramwelloq</div>
    <div class="abs social header-social"><span><i></i>Chatterly</span><span><i></i>Pipsong</span><span><i></i>Circlenet</span></div>
  </header>
  <nav class="abs main-nav">
    <a style="left:201px">About our School</a>
    <a style="left:332px">Risk Warning</a>
    <a style="left:440px">FAQ</a>
    <a style="left:488px">Trading Glossary</a>
    <a style="left:609px">Contact</a>
  </nav>

  <section class="abs hero" role="img" aria-label="Background photo of glowing stock market figures and charts"></section>
  <h1 class="abs hero-title">Learn to trade successfully</h1>
  <p class="abs hero-text">Lorem ipsum dolor sit amet, consectetur adipisicing elit, sed do eiusmod tempor incididunt ut labore et dolore magna aliqua. Ut enim ad mi sacoli stula por fador que so mazi na kalivradia.</p>
  <div class="abs btn hero-btn">Join us now</div>

  <section class="abs why">
    <div class="abs why-mark" aria-hidden="true">Bramwelloq</div>
    <h2 class="abs why-title">WHY TO JOIN US?</h2>
    <ul class="abs why-list">
      <li>*Best trading tips ever.</li>
      <li>*Secret tips from experts.</li>
      <li>*We teach you how to trade online.</li>
      <li>*Learn how to trade commodities.</li>
      <li>*Learn how to become a trader.</li>
    </ul>
  </section>

  <form class="abs signup">
    <h2>Join our school now!</h2>
    <div class="field" style="top:50px">First Name:</div>
    <div class="field" style="top:93px">Last Name:</div>
    <div class="field" style="top:137px">Email:</div>
    <div class="abs agree"><i></i>I agree with Terms &amp; Conditions</div>
    <div class="abs btn submit">Submit</div>
    <p class="abs member">Already a member?, <a>Sign in.</a></p>
  </form>

  <section class="abs offer">
    <h2 class="abs offer-title">WHAT WE OFFER</h2>
    <div class="abs card" style="left:27px;top:104px">
      <div class="card-photo" role="img" aria-label="Photo of a rising stock chart on a screen" style="background:linear-gradient(135deg,#2c6e8e,#0f2a3a 55%,#3aa0c8)"></div>
      <h3>Offering #1</h3>
      <p>Lorem ipsum dolor sit amet, consectetur adipisicing elit, sed do eiusmod tempor incidi-dunt ut labore et dolore magna aliqua. Ut enim ad mi.</p>
    </div>
    <div class="abs card" style="left:229px;top:104px">
      <div class="card-photo" role="img" aria-label="Photo of a city index ticker board at night" style="background:linear-gradient(135deg,#1a2a4a,#2c4c7a 45%,#c8a040)"></div>
      <h3>Offering #2</h3>
      <p>Lorem ipsum dolor sit amet, consectetur adipisicing elit, sed do eiusmod tempor incidi-dunt ut labore et dolore magna aliqua. Ut enim ad mi.</p>
    </div>
    <div class="abs card" style="left:429px;top:104px">
      <div class="card-photo" role="img" aria-label="Photo of a keyboard with a green online learning key" style="background:linear-gradient(160deg,#4a5058,#6fb83a 45%,#2e3338)"></div>
      <h3>Offering #3</h3>
      <p>Lorem ipsum dolor sit amet, consectetur adipisicing elit, sed do eiusmod tempor incidi-dunt ut labore et dolore magna aliqua. Ut enim ad mi.</p>
    </div>
    <div class="abs card" style="left:628px;top:104px">
      <div class="card-photo" role="img" aria-label="Photo of blue financial district towers" style="background:linear-gradient(135deg,#1e3a8a,#2a5cb0 50%,#b05060)"></div>
      <h3>Offering #4</h3>
      <p>Lorem ipsum dolor sit amet, consectetur adipisicing elit, sed do eiusmod tempor incidi-dunt ut labore et dolore magna aliqua. Ut enim ad mi.</p>
    </div>
  </section>

  <footer class="abs site-footer">
    <p class="abs copy">Copyright 2016 <b>Bramwelloq</b><small>All rights Reserved</small></p>
    <div class="abs social footer-social"><span><i></i>Chatterly</span><span><i></i>Pipsong</span><span><i></i>Circlenet</span></div>
    <p class="abs legal"><a>Terms &amp; Conditions</a> / <a>Privacy Protection</a></p>
  </footer>
</body>
</html>
```